Hot New Peruvian BBQ Concept, Tolen BBQ, Needs a Menu!!

A menu is needed for Tolen BBQ. Attached you will find the design of the menu I want. It is based on another bbq restaurant. I would like our menu to look very similar in format to the way the example looks. Our menu is also attached. I would like our menu items to be put in place of the sample's. Our logo will be available to add in by Monday. Tolen BBQ is a counter-serve, fast casual concept, taking the traditional American bbq concept and treating it with Peruvian flavor. We are a scratch-made kitchen using locally sourced and sustainably raised meats and vegetables.

Target Market(s)

large demographic, college kids to hipsters to baby boomers

Industry/Entity Type

Restaurant

Font styles to use
Other font styles liked:
• font being used for logo is 'Just Another Hand'. Open to suggestion on menu fonts..

Colors

Designer to choose colors to be used in the design.

Requirements
Must have
• Must be horizontal format. Needs to be an editable format. I want a blurb about our concept in place of the existing one on the supplied example. Blurb to be supplied tomorrow. Must have our logo in place of the one on the supplied link. Logo to be supplied. Must include my menu information in place of the existing on the supplied menu example.
Nice to have
• I would like to see a format similar to the one on the supplied link. It would be nice to have a similar pattern to the photo attached, in place of the existing 'decorative line- art' on the supplied menu example
Should not have
• Should not be a vertical format. Should not be anything other that what I've requested.

```html
<!DOCTYPE html>
<html lang="en">
<head>
<meta charset="utf-8">
<title>Tolen BBQ Menu Board</title>
<link href="https://fonts.googleapis.com/css2?family=Oswald:wght@400;500;700&family=Open+Sans:wght@400;600&family=Kaushan+Script&display=swap" rel="stylesheet">
<style>
:root{
  --page:#e4e4e4;
  --maroon-deep:#3a070a;
  --maroon:#6e0c10;
  --red:#c4141b;
  --red-bright:#e01a20;
  --white:#ffffff;
  --ink:#3a0a0c;
  --flame-a:#f7b12a;
  --flame-b:#e2461a;
}
*{box-sizing:border-box;margin:0;padding:0}
html,body{width:1200px;height:730px;overflow:hidden;background:var(--page)}
.menu-board{
  position:absolute;left:20px;top:35px;width:1160px;height:659px;overflow:hidden;
  background:linear-gradient(180deg,var(--maroon-deep) 0%,var(--maroon) 35%,var(--red) 75%,var(--red-bright) 100%);
  font-family:"Open Sans",sans-serif;color:var(--white);
  box-shadow:0 4px 12px rgba(0,0,0,.25);
}
.brand-block{position:absolute;left:0;top:0;width:289px;height:114px;text-align:center}
.produce-art{position:absolute;top:0;width:52px;height:114px;background:linear-gradient(160deg,#d83a22,#f2b51c 55%,#3f8a2a)}
.produce-art.left{left:0}.produce-art.right{right:0}
.brand-title{position:absolute;left:0;right:0;top:52px;font-family:"Oswald",sans-serif;font-weight:700;font-size:29px;line-height:1;letter-spacing:.5px}
.brand-sub{position:absolute;left:0;right:0;top:88px;font-family:"Kaushan Script",cursive;font-size:22px;line-height:1}
.brand-mode{position:absolute;left:0;width:289px;top:128px;text-align:center;font-family:"Oswald",sans-serif;font-size:14px;letter-spacing:.5px}
.brand-mode span{border-bottom:1px dashed var(--white);padding:0 4px 2px}
.brand-mode::before,.brand-mode::after{content:"";display:inline-block;width:24px;border-top:1.5px solid var(--white);vertical-align:middle;margin:0 6px}
.brand-name{position:absolute;left:0;width:289px;top:360px;text-align:center;font-family:"Oswald",sans-serif;font-weight:700;font-size:44px;line-height:52px;color:var(--white)}
.flame-band{position:absolute;left:0;right:0;bottom:0;height:140px;background:linear-gradient(180deg,rgba(226,70,26,0) 0%,var(--flame-b) 45%,var(--flame-a) 100%)}
.grill-art{position:absolute;left:400px;top:471px;width:226px;height:190px;border-radius:6px;background:linear-gradient(180deg,#5a5a5a,#c94a22 50%,#8a4a2a)}
.headline{position:absolute;left:328px;top:19px;width:359px;height:79px;background:var(--white);color:var(--ink);text-align:center;border-radius:4px;padding-top:6px}
.headline::before{content:"";position:absolute;inset:3px;border:1.5px solid var(--ink);border-radius:3px}
.headline .line-a{font-family:"Oswald",sans-serif;font-weight:500;font-size:17px;line-height:20px}
.headline .line-b{font-size:12px;line-height:16px}
.headline .line-c{font-family:"Oswald",sans-serif;font-weight:700;font-size:19px;line-height:24px}
.includes{position:absolute;left:290px;top:127px;width:434px;text-align:center;font-size:12.5px;white-space:nowrap}
.panel{position:absolute;border:2px solid var(--white);border-radius:4px;background:rgba(90,6,10,.35)}
.panel-title{position:relative;background:var(--white);color:var(--ink);text-align:center;font-family:"Oswald",sans-serif;font-weight:700;font-size:18px;height:28px;line-height:28px}
.panel-title::after{content:"";position:absolute;left:0;right:0;bottom:-6px;height:6px;background:linear-gradient(135deg,var(--white) 50%,transparent 50%) 0 0/8px 6px,linear-gradient(225deg,var(--white) 50%,transparent 50%) 0 0/8px 6px;background-repeat:repeat-x}
.items{list-style:none;padding:16px 6px 0 8px}
.item{display:flex;justify-content:space-between;font-size:7.4px;line-height:9px}
.item .desc{flex:0 0 140px}
.item .price{min-width:18px;text-align:right}
.plates{left:308px;top:162px;width:189px;height:277px}
.plates .item{height:40px;justify-content:flex-start}
.plates .item.short{height:32px}
.plates .desc{flex:0 0 120px}
.plates .price{text-align:left}
.plates .item.wide-price .desc{flex:0 0 84px}
.plates .item.wide-price .price{white-space:nowrap}
.sandwiches{left:518px;top:162px;width:188px;height:277px}
.sandwiches .item{margin-bottom:10px}
.sandwiches .desc{flex:0 0 150px}
.sandwich-note{text-align:center;font-size:7.4px;line-height:9px;padding:2px 12px}
.sandwich-art{position:absolute;left:11px;top:161px;width:166px;height:93px;border-radius:40% 40% 30% 30%;background:linear-gradient(180deg,#b98a55,#d25a4a 50%,#8c5c36)}
.sides{left:742px;top:19px;width:189px;height:218px}
.sides .item{height:31px}
.sauces{left:952px;top:19px;width:189px;height:218px}
.sauce-list{padding-top:19px}
.sauce{text-align:center;font-size:7.4px;line-height:9px;height:32px}
.sauce-price{position:absolute;left:43px;top:170px;width:100px;height:32px;border-radius:16px;background:var(--white);color:var(--ink);text-align:center;font-family:"Oswald",sans-serif;font-weight:700;font-size:26px;line-height:32px}
.snacks{left:742px;top:268px;width:189px;height:215px}
.snacks .item{height:31px}
.snacks .item.tall{height:40px}
.feast{position:absolute;left:953px;top:268px;width:187px;height:41px;background:var(--white);color:var(--ink);text-align:center;border-radius:3px;padding-top:3px}
.feast .f-a{font-family:"Oswald",sans-serif;font-weight:500;font-size:9px;line-height:12px}
.feast .f-b{font-size:6.5px;line-height:9px}
.feast .f-c{font-family:"Oswald",sans-serif;font-size:8.5px;line-height:12px}
.sweet{left:952px;top:325px;width:189px;height:158px}
.sweet .item{height:32px}
.cookie-art{position:absolute;left:36px;top:110px;width:128px;height:36px;border-radius:18px;background:linear-gradient(90deg,#3a2a1a,#e8a24a 45%,#2a1a14)}
.sourcing{position:absolute;left:762px;top:520px;width:358px;height:67px;background:var(--white);color:var(--red);text-align:center;border-radius:4px;padding-top:6px}
.sourcing::before{content:"";position:absolute;inset:3px;border:1.5px solid var(--red);border-radius:3px}
.sourcing .s-a{font-family:"Oswald",sans-serif;font-size:11px;line-height:15px}
.sourcing .s-b{font-size:8.5px;line-height:13px}
.sourcing .s-c{font-family:"Oswald",sans-serif;font-weight:700;font-size:19px;line-height:26px}
</style>
</head>
<body>
<main class="menu-board">
  <div class="flame-band" role="img" aria-label="Flames rising along the bottom edge with a red chili pepper"></div>

  <header class="brand-block">
    <div class="produce-art left" role="img" aria-label="Fresh tomatoes, peppers and herbs"></div>
    <div class="produce-art right" role="img" aria-label="Fresh tomatoes, peppers and herbs"></div>
    <div class="brand-title">BBQ RESTAURENT</div>
    <div class="brand-sub">Grilled . Smoked</div>
  </header>
  <div class="brand-mode"><span>COUNTER-SERVE</span></div>

  <div class="brand-name">Tolen BBQ</div>

  <section class="headline">
    <div class="line-a">CHEF DRIVEN, COUNTER - SERVE RESTAURANT</div>
    <div class="line-b">FEATURING PERUVIAN INSPIRED</div>
    <div class="line-c">GRILLED &amp; SMOKED MEATS AND SIDE DISHES</div>
  </section>
  <p class="includes">Includes pan de choclo, salsa criolla, choice of 2 sides &amp; 2 sauces</p>

  <section class="panel plates">
    <h2 class="panel-title">· PLATES ·</h2>
    <ul class="items">
      <li class="item wide-price"><span class="desc">Pollo a la Brasa<br>( Marinated &amp; grilled free-range chicken )</span><span class="price">12 qtr dark / 13 qtr white</span></li>
      <li class="item"><span class="desc">Costilla<br>( Beef rib, black pepper &amp; coriander )</span><span class="price">22</span></li>
      <li class="item"><span class="desc">Salchicha<br>( Pork sausage link, aji panca &amp; achiote )</span><span class="price">12</span></li>
      <li class="item short"><span class="desc">Carne<br>( Beef brisket, coffee &amp; cocoa )</span><span class="price">14</span></li>
      <li class="item"><span class="desc">Verduras<br>( Seasonal vegetables, chimichurri sauce )</span><span class="price">11</span></li>
      <li class="item"><span class="desc">Chanchito<br>( Pulled pork, cumin &amp; brown sugar )</span><span class="price">13</span></li>
    </ul>
  </section>

  <section class="panel sandwiches">
    <h2 class="panel-title">· SANDWICHES ·</h2>
    <ul class="items">
      <li class="item"><span class="desc">Pulled Pork OR Pork Sausage</span><span class="price">10</span></li>
      <li class="item"><span class="desc">Beef Brisket</span><span class="price">12</span></li>
    </ul>
    <p class="sandwich-note">Served on a ciabatta roll with salsa criolla, choice of 1 side &amp; 1 sauce</p>
    <div class="sandwich-art" role="img" aria-label="Photo of a ciabatta sandwich with meat and greens"></div>
  </section>

  <div class="grill-art" role="img" aria-label="Illustration of sausages on a grill with tongs"></div>

  <section class="panel sides">
    <h2 class="panel-title">· SIDES ·</h2>
    <ul class="items">
      <li class="item"><span class="desc">Arroz con Frijoles ( Garlic rice &amp; peruvian beans )</span><span class="price">5</span></li>
      <li class="item"><span class="desc">Maccarones con Queso ( Elbow pasta, aji amarillo cheese sauce )</span><span class="price">5</span></li>
      <li class="item"><span class="desc">Ensalada de Col ( Cabbage &amp; carrot slaw, cilantro-lime vinaigrette )</span><span class="price">3</span></li>
      <li class="item"><span class="desc">Salsa Criolla ( lime &amp; aji pickled red onion, cilantro )</span><span class="price">3</span></li>
      <li class="item"><span class="desc">Ensaladilla Papas ( Potato salad, kalamata aioli, hard egg )</span><span class="price">5</span></li>
    </ul>
  </section>

  <section class="panel sauces">
    <h2 class="panel-title">· SAUCES ·</h2>
    <div class="sauce-list">
      <p class="sauce">Aji Limo. spicy, vinegar base</p>
      <p class="sauce">Aji Mirasol. mild heat, mustard base</p>
      <p class="sauce">Aji Panca. smoky, sweet, little spicy</p>
      <p class="sauce">Nikkei. tamarind, soy, honey</p>
    </div>
    <span class="sauce-price">50 ea</span>
  </section>

  <section class="panel snacks">
    <h2 class="panel-title">· SNACKS ·</h2>
    <ul class="items">
      <li class="item tall"><span class="desc">Cebiche ( Marinated local fish, leche de tigre, red onion, sweet potato, cancha, cilantro )</span><span class="price">10</span></li>
      <li class="item"><span class="desc">Anticucho ( Grilled spanish octopus, aji panca salsa, potato, chimichurri )</span><span class="price">10</span></li>
      <li class="item"><span class="desc">Empanada ( Pastry pocket, inquire about today's )</span><span class="price">6</span></li>
      <li class="item"><span class="desc">Yuca Frita ( Fried cassava 'fries', salsa golf )</span><span class="price">6</span></li>
      <li class="item"><span class="desc">Lechuga ( Field greens, radish, carrot, salsa criolla, buttermilk dressing or sherry vinaigrette )</span><span class="price">5</span></li>
    </ul>
  </section>

  <section class="feast">
    <div class="f-a">PACHAMANCA. ALL THE MEATS, ALL THE SIDES,</div>
    <div class="f-b">ALL THE SAUCES 70</div>
    <div class="f-c">( FEEDS 5 - 6 PEOPLE )</div>
  </section>

  <section class="panel sweet">
    <h2 class="panel-title">· SWEET ·</h2>
    <ul class="items">
      <li class="item"><span class="desc">Helado ( Housemade soft-serve ice cream, inquire about today's flavors )</span><span class="price">4</span></li>
      <li class="item"><span class="desc">Alfajores ( Shortbread &amp; dulce de leche sandwich cookies, powdered sugar )</span><span class="price">4</span></li>
    </ul>
    <div class="cookie-art" role="img" aria-label="Assorted cookies"></div>
  </section>

  <section class="sourcing">
    <div class="s-a">WE SOURCE HIGH QUALITY, NATURALLY RAISED &amp; HORMONE FREE MEATS</div>
    <div class="s-b">WE USE LOCAL, ORGANIC PRODUCE &amp; INGREDIENTS WHEREVER POSSIBLE</div>
    <div class="s-c">WE SUPPORT LOCAL BUSINESSES</div>
  </section>
</main>
</body>
</html>
```